Hartwell Systems Advisory - IT Consultancy

I already have a Wordpress site, but not happy with the look and feel or the template I chose.
I want a site as a web presence only, I can configure base SEO myself, but most business is referrals not from a search, so low priority.

My current site is http://hartsys.example where you can see the sort of content I already have.

Target Market(s)

Business to Business services.

Industry/Entity Type

Consulting

Font styles to use
Sans Serif

Colors
3277b5

Requirements
Must have
• Front Page Template
• Freephone number on front page.
• My Logo and the Brevanta logo on the front page
• Page template for Services, Solutions and Portfolio
• Contact Page
• Ability to embed links to Video clips hosted by a third party
Nice to have
• Each page could have a side bar with some common functions, like Request Demo.
• Second Contact Page specifically to Request Demonstrations of Brevanta Products, the demo contact page needs to capture some additional information in text boxes and also a check box list of features. The list of features needs to be easily configurable.
• Features to include in checkbox list.
• Contract Management
• Service Desk
• Document Management
• Contract Management
• Business Workflow

```html
<!DOCTYPE html>
<html lang="en">
<head>
<meta charset="utf-8">
<title>Hartwell Systems Advisory</title>
<link href="https://fonts.googleapis.com/css2?family=Open+Sans:wght@400;600;700&family=Lato:wght@300;400;700&display=swap" rel="stylesheet">
<style>
:root{
  --brand:#3277b5;
  --brand-dark:#1d5690;
  --navy:#0e2a4d;
  --navy-deep:#0a1f3a;
  --accent:#f5a31a;
  --ink:#333a42;
  --muted:#7a828b;
  --line:#e1e4e8;
  --paper:#ffffff;
  --mist:#f2f3f5;
  --grey-band:#e6e7e9;
}
*{margin:0;padding:0;box-sizing:border-box}
html,body{width:1200px;height:2192px;overflow:hidden;background:var(--paper)}
body{font-family:"Open Sans",Arial,sans-serif;color:var(--ink);position:relative}
a{color:inherit;text-decoration:none}

/* Header + hero */
.hero{position:absolute;top:0;left:0;width:1200px;height:512px}
.hero-photo{position:absolute;inset:0;background:linear-gradient(160deg,#5d93c4 0%,#3d78b0 40%,#2a5f95 75%,#1f4c7c 100%)}
.hero-tint{position:absolute;inset:0;background:linear-gradient(180deg,rgba(18,52,92,.55) 0%,rgba(50,119,181,.25) 30%,rgba(50,119,181,.35) 100%)}
.site-header{position:absolute;top:0;left:0;width:1200px;height:100px;display:flex;align-items:center;padding:0 160px}
.brand{color:#fff;font-family:"Lato",sans-serif}
.brand-name{font-size:34px;font-weight:700;letter-spacing:2px;line-height:1}
.brand-tag{font-size:10px;letter-spacing:2.5px;margin-top:4px}
.main-nav{margin-left:auto;display:flex;gap:28px;align-items:center;color:#fff;font-size:13px;font-weight:600}
.main-nav .phone{display:flex;align-items:center;gap:6px}
.hero-copy{position:absolute;top:240px;left:0;width:1200px;text-align:center;color:#fff;font-family:"Lato",sans-serif}
.hero-title{font-size:56px;font-weight:400}
.hero-sub{font-size:30px;font-weight:300;margin-top:8px}
.slider-dots{position:absolute;top:516px;left:0;width:1200px;display:flex;justify-content:center;gap:8px}
.slider-dots span{width:14px;height:14px;border-radius:50%;background:#d9dce0}
.slider-dots span.on{background:var(--accent)}

/* Call bar */
.callout{position:absolute;top:556px;left:0;width:1200px;height:72px;background:var(--mist);border-top:1px solid var(--line);border-bottom:1px solid var(--line);display:flex;align-items:center;justify-content:center;gap:36px}
.callout-text{font-size:21px;color:var(--ink)}
.btn-accent{background:var(--accent);color:#fff;font-size:14px;font-weight:600;padding:12px 34px;border-radius:2px}

/* Services */
.services{position:absolute;top:676px;left:150px;width:900px;display:flex;gap:20px}
.service-card{flex:1;height:240px;border:1px solid var(--line);background:#fff;padding:20px 20px 18px;box-shadow:0 1px 4px rgba(0,0,0,.06);display:flex;flex-direction:column}
.service-icon{width:48px;height:48px;margin-bottom:12px;flex:none}
.service-title{color:var(--brand);font-size:15px;font-weight:600;margin-bottom:8px;white-space:nowrap}
.service-text{font-size:11.5px;line-height:1.55;color:var(--muted)}
.service-card .more{margin-top:auto}
.more{font-size:11px;font-weight:700;color:var(--navy)}

/* About */
.about{position:absolute;top:930px;left:0;width:1200px;height:420px}
.about-bg{position:absolute;inset:0}
.about-inner{position:absolute;top:100px;left:160px;width:880px;display:flex;gap:40px}
.about-copy{flex:1;color:#fff}
.about-title{font-family:"Lato",sans-serif;font-size:38px;font-weight:700;line-height:1}
.about-sub{font-family:"Lato",sans-serif;font-size:22px;margin:4px 0 14px}
.about-copy p{font-size:12.5px;line-height:1.6;color:#c9d8ea;margin-bottom:12px}
.video{width:380px;height:220px;position:relative}
.video-frame{position:absolute;inset:0;background:linear-gradient(135deg,#c8d3dd 0%,#9fb2c4 50%,#6d879f 100%)}
.video-play{position:absolute;left:165px;top:85px}
.video-bar{position:absolute;left:0;bottom:0;width:100%;height:26px;background:rgba(10,31,58,.85);display:flex;align-items:center;padding:0 10px;gap:10px}
.video-track{flex:1;height:4px;background:#5a7088}
.video-track span{display:block;width:30%;height:100%;background:var(--brand)}

/* News */
.news{position:absolute;top:1398px;left:160px;width:880px}
.section-title{font-family:"Lato",sans-serif;font-size:30px;color:var(--brand);font-weight:400;border-bottom:1px solid var(--line);padding-bottom:10px;margin-bottom:22px}
.news-grid{display:flex;gap:30px}
.news-card{flex:1}
.news-photo{height:138px}
.news-title{font-size:15px;font-weight:600;color:var(--ink);margin:14px 0 8px}
.news-text{font-size:12px;line-height:1.6;color:var(--muted);margin-bottom:10px}

/* Testimonials */
.testimonials{position:absolute;top:1770px;left:0;width:1200px;height:280px;background:var(--grey-band);text-align:center}
.testimonials h2{font-family:"Lato",sans-serif;font-size:26px;color:var(--ink);font-weight:400;letter-spacing:1px;padding-top:28px}
.quote{position:relative;width:840px;margin:22px auto 0}
.quote-mark{position:absolute;left:-40px;top:-22px;font-family:"Lato",sans-serif;font-size:64px;color:#9aa1a9}
.quote p{font-size:13px;line-height:1.65;color:#5b636b;font-style:italic}
.quote-author{margin-top:16px;font-size:12px;color:var(--ink)}
.quote-role{font-size:11px;color:var(--muted)}

/* Footer */
.site-footer{position:absolute;top:2050px;left:0;width:1200px;height:142px;background:var(--navy-deep);color:#fff}
.footer-inner{position:absolute;top:36px;left:160px;width:880px;display:flex;align-items:flex-start}
.footer-nav{display:flex;gap:22px;font-size:12px;font-weight:600}
.footer-copy{font-size:11px;color:#8a9bb0;margin-top:14px}
.social{display:flex;gap:8px;margin:30px 0 0 110px}
.social span{width:24px;height:24px;border-radius:50%;border:1px solid #fff}
.partner{margin-left:auto;text-align:right}
.partner-name{display:flex;align-items:center;gap:8px;font-size:28px;font-weight:700;color:#fff}
.partner-name i{width:16px;height:16px;background:var(--accent);display:block}
.partner-tier{font-size:13px;color:#fff;margin-top:2px}
</style>
</head>
<body>

<section class="hero">
  <div class="hero-photo" role="img" aria-label="Business team working together at a table with laptops"></div>
  <div class="hero-tint"></div>
  <header class="site-header">
    <div class="brand">
      <div class="brand-name">HARTWELL</div>
      <div class="brand-tag">SYSTEMS ADVISORY</div>
    </div>
    <nav class="main-nav">
      <a href="#">ABOUT</a>
      <a href="#">SERVICES</a>
      <a href="#">BREVANTA SOLUTION</a>
      <a href="#">BLOG</a>
      <a href="#">CONTACT</a>
      <span class="phone">
        <svg width="14" height="14" viewBox="0 0 24 24"><path fill="#fff" d="M6.6 10.8a15 15 0 0 0 6.6 6.6l2.2-2.2c.3-.3.7-.4 1-.2 1.1.4 2.3.6 3.6.6.6 0 1 .4 1 1V20c0 .6-.4 1-1 1A17 17 0 0 1 3 4c0-.6.4-1 1-1h3.5c.6 0 1 .4 1 1 0 1.3.2 2.5.6 3.6.1.3 0 .7-.2 1z"/></svg>
        +44 0800 555 0199
      </span>
    </nav>
  </header>
  <div class="hero-copy">
    <h1 class="hero-title">Project Management &amp; Solution</h1>
    <p class="hero-sub">Duis quam nam eget lacus Aliquam</p>
  </div>
</section>
<div class="slider-dots"><span class="on"></span><span></span><span></span><span></span></div>

<section class="callout">
  <span class="callout-text">Fusce ultricies orci ac feugiat suscipit leo massa</span>
  <a class="btn-accent" href="#">Request Demo</a>
</section>

<section class="services">
  <article class="service-card">
    <svg class="service-icon" viewBox="0 0 56 56"><g fill="#f5a31a"><rect x="8" y="34" width="8" height="14"/><rect x="20" y="26" width="8" height="22"/><rect x="32" y="18" width="8" height="30"/><rect x="44" y="10" width="8" height="38"/></g><rect x="4" y="48" width="50" height="2" fill="#0e2a4d"/></svg>
    <h3 class="service-title">Project Management</h3>
    <p class="service-text">Plan every phase with clear milestones and steady reports that keep delivery on track.</p>
    <a class="more" href="#">LEARN MORE</a>
  </article>
  <article class="service-card">
    <svg class="service-icon" viewBox="0 0 56 56"><g fill="#f5a31a"><rect x="6" y="6" width="20" height="20"/><rect x="30" y="6" width="20" height="20"/><rect x="6" y="30" width="20" height="20"/></g><rect x="30" y="30" width="20" height="20" fill="#0e2a4d"/></svg>
    <h3 class="service-title">Solution Design</h3>
    <p class="service-text">Shape systems around the way you work, joining tools and data into one process.</p>
    <a class="more" href="#">LEARN MORE</a>
  </article>
  <article class="service-card">
    <svg class="service-icon" viewBox="0 0 56 56"><g fill="#f5a31a"><circle cx="14" cy="18" r="6"/><circle cx="28" cy="14" r="7"/><circle cx="42" cy="18" r="6"/><rect x="6" y="28" width="16" height="16" rx="3"/><rect x="20" y="24" width="16" height="20" rx="3"/><rect x="34" y="28" width="16" height="16" rx="3"/></g><rect x="4" y="44" width="48" height="4" fill="#0e2a4d"/></svg>
    <h3 class="service-title">Consulting</h3>
    <p class="service-text">Practical advice from people who have run projects, with honest review of risks.</p>
    <a class="more" href="#">LEARN MORE</a>
  </article>
  <article class="service-card">
    <svg class="service-icon" viewBox="0 0 56 56"><g fill="#f5a31a"><rect x="24" y="4" width="8" height="48"/><rect x="4" y="24" width="48" height="8"/><rect x="24" y="4" width="8" height="48" transform="rotate(45 28 28)"/><rect x="24" y="4" width="8" height="48" transform="rotate(-45 28 28)"/><circle cx="28" cy="28" r="16"/></g><circle cx="28" cy="28" r="7" fill="#fff"/></svg>
    <h3 class="service-title">Technology</h3>
    <p class="service-text">Choose, configure and support platforms that fit your business as it grows.</p>
    <a class="more" href="#">LEARN MORE</a>
  </article>
</section>

<section class="about">
  <svg class="about-bg" width="1200" height="420" viewBox="0 0 1200 420" preserveAspectRatio="none">
    <defs><linearGradient id="aboutGrad" x1="0" y1="0" x2="1" y2="1"><stop offset="0" stop-color="#0e2a4d"/><stop offset=".55" stop-color="#163c68"/><stop offset="1" stop-color="#0a1f3a"/></linearGradient></defs>
    <path d="M0 40 Q300 0 600 30 T1200 20 V400 Q900 430 600 405 T0 410 Z" fill="url(#aboutGrad)"/>
  </svg>
  <div class="about-inner">
    <div class="about-copy">
      <h2 class="about-title">ABOUT HARTWELL</h2>
      <div class="about-sub">TECHNOLOGY SOLUTION</div>
      <p>We help growing firms select, build and run the business systems they depend on, from first workshop through to live service and ongoing support for every team.</p>
      <p>Our consultants bring years of delivery experience, plain advice and a steady focus on outcomes that matter to your people and clients.</p>
    </div>
    <div class="video">
      <div class="video-frame" role="img" aria-label="Video still of two colleagues reviewing work on a laptop"></div>
      <svg class="video-play" width="50" height="50" viewBox="0 0 50 50"><circle cx="25" cy="25" r="24" fill="#0e2a4d" opacity=".85"/><path d="M20 15 L36 25 L20 35 Z" fill="#fff"/></svg>
      <div class="video-bar">
        <svg width="10" height="12" viewBox="0 0 10 12"><path d="M0 0 L10 6 L0 12 Z" fill="#fff"/></svg>
        <div class="video-track"><span></span></div>
      </div>
    </div>
  </div>
</section>

<section class="news">
  <h2 class="section-title">LATEST NEWS</h2>
  <div class="news-grid">
    <article class="news-card">
      <div class="news-photo" role="img" aria-label="Businessman sketching a growth chart" style="background:linear-gradient(135deg,#2f5f8c,#7a9bb8)"></div>
      <h3 class="news-title">Mauris vel lacus vitae felis vestib</h3>
      <p class="news-text">A short update on planning tools and how teams can plan work with less effort.</p>
      <a class="more" href="#">READ MORE</a>
    </article>
    <article class="news-card">
      <div class="news-photo" role="img" aria-label="Colleagues meeting around a desk" style="background:linear-gradient(135deg,#b9c4cc,#7e8f9c)"></div>
      <h3 class="news-title">Duis quam Nam eget lacus Aliquam</h3>
      <p class="news-text">Notes from a recent rollout and the lessons our clients found most useful.</p>
      <a class="more" href="#">READ MORE</a>
    </article>
    <article class="news-card">
      <div class="news-photo" role="img" aria-label="Hand holding a glowing network graphic" style="background:linear-gradient(135deg,#1c4f86,#5fa0d6)"></div>
      <h3 class="news-title">Aenena in gravida eu mattis</h3>
      <p class="news-text">Why connected workflows save time and keep every document in its right place.</p>
      <a class="more" href="#">READ MORE</a>
    </article>
  </div>
</section>

<section class="testimonials">
  <h2>TESTIMONIALS</h2>
  <div class="quote">
    <span class="quote-mark">&ldquo;</span>
    <p>Hartwell Systems Advisory delivered the project on time and on budget. We were impressed by how they listened, explained each choice and kept our team informed. The system they built is clear, robust and simple to use, and support has been quick whenever we needed help. We are working with them again this year.</p>
    <div class="quote-author">Daniel Ashford</div>
    <div class="quote-role">Company Manager</div>
  </div>
</section>

<footer class="site-footer">
  <div class="footer-inner">
    <div>
      <nav class="footer-nav">
        <a href="#">ABOUT</a><a href="#">SERVICES</a><a href="#">BREVANTA SOLUTION</a><a href="#">BLOG</a><a href="#">CONTACT</a>
      </nav>
      <div class="footer-copy">© 2016 Company Name. All rights Reserved. Terms of use</div>
    </div>
    <div class="social"><span></span><span></span><span></span><span></span></div>
    <div class="partner">
      <div class="partner-name"><i></i>Brevanta</div>
      <div class="partner-tier">Gold Partner</div>
    </div>
  </div>
</footer>

</body>
</html>
```